Harbor Kindness Inc

We need a full re-design of our non-profit organization website (www.harborkindness.org). Ideally, we are looking to make it more attractive, user-friendly, and interactive with our business model.

Please make sure to user colors that ago with our logo.

We need a homepage done and we also need a content page done where we will use for the other pages to fill with content.

Target Market(s)

Clothes/textiles donations.

Industry/Entity Type

Charity

Number of Pages Required

2 page

Colors

Designer to choose colors to be used in the design.

Requirements
Must have
• It must match the styling of our logo and same colors as current website. (www.harborkindness.org)
Nice to have
• Sleek homepage that is easy to understand and get our main points across.

```html
<!DOCTYPE html>
<html lang="en">
<head>
<meta charset="utf-8">
<title>Sponsors – Harbor Kindness Inc</title>
<link href="https://fonts.googleapis.com/css2?family=Montserrat:wght@500;600;700&family=Open+Sans:wght@400;600;700&display=swap" rel="stylesheet">
<style>
:root{
  --yellow:#f7c21a;
  --gold:#d9b30f;
  --leaf:#4c7a1c;
  --green:#2f8a1f;
  --green-dark:#175c10;
  --orange:#f39a12;
  --ink:#222;
  --text:#555;
  --white:#fff;
}
*{margin:0;padding:0;box-sizing:border-box}
html,body{width:682px;height:1200px;overflow:hidden;background:var(--white)}
body{position:relative;font-family:"Open Sans",sans-serif;color:var(--text)}
.top-bar{position:absolute;left:0;top:0;width:682px;height:3px;background:var(--yellow)}
.phone-tab{position:absolute;left:509px;top:0;width:105px;height:26px;background:var(--yellow);border-radius:0 0 3px 3px;display:flex;align-items:center;justify-content:center;gap:4px;font:700 10.5px "Open Sans",sans-serif;color:var(--ink)}
.header{position:absolute;left:0;top:3px;width:682px;height:64px}
.brand{position:absolute;left:68px;top:24px;display:flex;align-items:center;gap:6px}
.brand-mark{width:22px;height:22px;background:var(--leaf);border-radius:3px}
.brand-name{font:700 12px "Montserrat",sans-serif;color:var(--green-dark);line-height:1}
.brand-tag{font:400 6.5px "Open Sans",sans-serif;color:var(--ink);margin-top:2px}
.nav{position:absolute;left:228px;top:28px;display:flex;align-items:center;gap:14px;font:500 10.5px "Open Sans",sans-serif;color:var(--ink)}
.nav-home{width:20px;height:20px;border-radius:50%;background:var(--green);display:flex;align-items:center;justify-content:center;margin-right:-2px}
.hero{position:absolute;left:0;top:67px;width:682px;height:263px;overflow:hidden}
.hero-photo{position:absolute;inset:0;background:linear-gradient(180deg,#5f7d45 0%,#8a9a7c 45%,#9c9a94 75%,#7f7a6e 100%)}
.hero-title{position:absolute;left:0;top:85px;width:682px;text-align:center;font:700 32px "Montserrat",sans-serif;color:var(--white);letter-spacing:.5px}
.hero-curve{position:absolute;left:0;top:0}
.intro{position:absolute;left:71px;top:338px;width:526px}
.intro h1{font:600 21px "Montserrat",sans-serif;color:var(--ink);margin-bottom:8px}
.intro p{font-size:7.7px;line-height:13.3px;color:var(--text)}
.card{position:absolute;width:171px;height:160px;background:linear-gradient(180deg,var(--gold) 0%,#8f9a16 50%,var(--leaf) 100%);box-shadow:0 1px 3px rgba(0,0,0,.25);text-align:center;color:var(--white);font-size:7.4px;line-height:13px}
.cert{position:absolute;left:37px;top:-32px;width:99px;height:71px;background:#f4f1e8;border:3px solid #7fae7f;box-shadow:0 1px 3px rgba(0,0,0,.3)}
.card-title{position:absolute;left:8px;right:8px;top:48px;font-weight:700;font-size:7.4px;line-height:9.5px}
.card-body{position:absolute;left:10px;right:10px;top:72px}
.more{position:absolute;left:327px;top:937px}
.footer{position:absolute;left:0;top:987px;width:682px;height:213px;background:var(--green);color:var(--white)}
.col{position:absolute;top:30px}
.col h3{font:500 10.5px "Montserrat",sans-serif;margin-bottom:12px;text-transform:uppercase}
.col li{list-style:none;font-size:8px;line-height:16px}
.divider{position:absolute;top:30px;width:1px;height:93px;background:rgba(255,255,255,.25)}
.contact-line{display:flex;gap:7px;font-size:8px;line-height:15.5px}
.zip{width:149px;height:21px;background:var(--green-dark);font-size:7.5px;padding:5px 10px;color:#dfe}
.search{margin-top:6px;width:71px;height:22px;background:var(--orange);font:600 10px "Open Sans",sans-serif;display:flex;align-items:center;justify-content:center}
.social{display:flex;gap:3px;margin-top:7px}
.social span{width:22px;height:22px;border:1.5px solid var(--white);border-radius:50%}
.rule{position:absolute;left:72px;top:175px;width:536px;height:1px;background:rgba(255,255,255,.25)}
.copy{position:absolute;left:0;top:186px;width:682px;text-align:center;font-size:7px;color:#bfe0b4}
</style>
</head>
<body>
<div class="top-bar"></div>
<header class="header">
  <div class="brand">
    <span class="brand-mark"></span>
    <div><div class="brand-name">HARBOR KINDNESS</div><div class="brand-tag">Think Globally while Donating Locally</div></div>
  </div>
  <nav class="nav">
    <span class="nav-home"><svg width="10" height="10" viewBox="0 0 10 10"><path d="M5 1 L9.5 5 H8 V9 H6 V6.5 H4 V9 H2 V5 H0.5 Z" fill="#fff"/></svg></span>
    <span>Mission</span><span>Family</span><span>How it Works</span><span>About Us</span><span>News</span><span>Donate</span><span>Sponsors</span>
  </nav>
</header>
<div class="phone-tab"><svg width="10" height="10" viewBox="0 0 10 10"><path d="M2 0.5 L4 2.8 L3 4 Q4 6 6 7 L7.2 6 L9.5 8 L8.3 9.5 Q4.5 9.5 0.5 1.7 Z" fill="#2f6a12"/></svg>(855) 410-3388</div>

<section class="hero">
  <div class="hero-photo" role="img" aria-label="Smiling volunteers in grey shirts holding donation boxes in a park"></div>
  <h2 class="hero-title">SPONSORS</h2>
  <svg class="hero-curve" width="682" height="263" viewBox="0 0 682 263">
    <path d="M0 263 Q300 186 682 255 L682 263 Z" fill="#f7c21a"/>
    <path d="M0 264 Q300 196 682 260 L682 264 Z" fill="#fff"/>
  </svg>
</section>

<section class="intro">
  <h1>Sponsors</h1>
  <p>We are working hard to get more businesses involved with our mission to help local communities by placing clothing donation bins on their property. It is not much to ask for &nbsp;5X5 feet of space. However, combining all the locations will make Harbor Kindness organization bigger and stronger. We will disclose all business sponsors on our website for the public to recognize who they are and their humble contributions. However, with the combination of all the locations, the Harbor Kindness organization becomes bigger and stronger.<br>If you are looking to make a financial donation in the form of a check, please make it payable to “Harbor Kindness Inc” Please include your address inside the envelope and we will send you an IRS tax exemption for the amount donated. Thank you for supporting Harbor Kindness and your local community.You will have an option to be hosted as a donor on the website.</p>
</section>

<article class="card" style="left:77px;top:541px">
  <div class="cert" role="img" aria-label="Certificate of thanks for Greenleaf Grill"></div>
  <div class="card-title">Harbor Kindness is very grateful<br>to Greenleaf Grill</div>
  <div class="card-body">https://greenleafgrill.com/<br>72 Orchard Ln, Hudson, NY 12534<br>518-555-0142<br>for helped with place a donation box on their property.</div>
</article>
<article class="card" style="left:259px;top:541px">
  <div class="cert" role="img" aria-label="Certificate of thanks for R and M Builders"></div>
  <div class="card-title">Harbor Kindness is very grateful to</div>
  <div class="card-body" style="top:72px">R and M Builders<br>Catskill NY 12414<br>518-555-0178<br>for helped with place a clothing collection been on their property.</div>
</article>
<article class="card" style="left:444px;top:541px">
  <div class="cert" role="img" aria-label="Certificate of thanks for Lantern Pizza"></div>
  <div class="card-title">LANTERN PIZZA</div>
  <div class="card-body">14 Main St, Hudson, NY 12534<br>tel. 518-555-0119<br>http://www.lanternpizzahudson.com/<br>for participation in charity project and helped with place a donation box on their</div>
</article>

<article class="card" style="left:77px;top:759px">
  <div class="cert" role="img" aria-label="Certificate of thanks for Greenleaf Grill"></div>
  <div class="card-title">Harbor Kindness is very grateful<br>to Greenleaf Grill</div>
  <div class="card-body">https://greenleafgrill.com/<br>72 Orchard Ln, Hudson, NY 12534<br>518-555-0142<br>for helped with place a donation box on their property.</div>
</article>
<article class="card" style="left:259px;top:759px">
  <div class="cert" role="img" aria-label="Certificate of thanks for R and M Builders"></div>
  <div class="card-title">Harbor Kindness is very grateful to</div>
  <div class="card-body">R and M Builders<br>Catskill NY 12414<br>518-555-0178<br>for helped with place a clothing collection been on their property.</div>
</article>
<article class="card" style="left:444px;top:759px">
  <div class="cert" role="img" aria-label="Certificate of thanks for Lantern Pizza"></div>
  <div class="card-title">LANTERN PIZZA</div>
  <div class="card-body">14 Main St, Hudson, NY 12534<br>tel. 518-555-0119<br>http://www.lanternpizzahudson.com/<br>for participation in charity project and helped with place a donation box on their</div>
</article>

<svg class="more" width="26" height="26" viewBox="0 0 26 26">
  <circle cx="13" cy="13" r="12" fill="none" stroke="#555" stroke-width="1.2"/>
  <path d="M8 11 L13 16 L18 11" fill="none" stroke="#555" stroke-width="1.8"/>
</svg>

<footer class="footer">
  <div class="col" style="left:66px"><h3>Quick Links</h3><ul><li>About Us</li><li>Mission</li><li>Family</li><li>How it Works</li></ul></div>
  <div class="divider" style="left:150px"></div>
  <div class="col" style="left:177px"><h3>Resources</h3><ul><li>News</li><li>Donate</li><li>Sponsors</li><li>Contact Us</li></ul></div>
  <div class="divider" style="left:258px"></div>
  <div class="col" style="left:287px"><h3>Contact Us</h3>
    <div class="contact-line"><svg width="8" height="11" viewBox="0 0 8 11"><path d="M4 0.5 A3.5 3.5 0 0 1 7.5 4 Q7.5 6 4 10.5 Q0.5 6 0.5 4 A3.5 3.5 0 0 1 4 0.5 Z" fill="#fff"/><circle cx="4" cy="4" r="1.3" fill="#2f8a1f"/></svg><span>9 Maple CT Coxsackie<br>NY 12051</span></div>
    <div class="contact-line"><svg width="9" height="9" viewBox="0 0 10 10"><path d="M2 0.5 L4 2.8 L3 4 Q4 6 6 7 L7.2 6 L9.5 8 L8.3 9.5 Q4.5 9.5 0.5 1.7 Z" fill="#fff"/></svg><span>518.555.0163</span></div>
    <div class="contact-line"><svg width="9" height="8" viewBox="0 0 9 8"><rect x="0" y="1" width="9" height="6.5" fill="#fff"/><path d="M0 1 L4.5 4.5 L9 1" fill="none" stroke="#2f8a1f" stroke-width=".9"/></svg><span>info@harborkindness.org</span></div>
  </div>
  <div class="divider" style="left:432px"></div>
  <div class="col" style="left:456px"><h3>Find Donation Place</h3>
    <div class="zip">Zip Code</div>
    <div class="search">Search</div>
    <div class="social" aria-label="Social links"><span></span><span></span><span></span><span></span></div>
  </div>
  <div class="rule"></div>
  <div class="copy">© 2018 Company Name &nbsp;All right reserved</div>
</footer>
</body>
</html>
```